Zielgruppe
Wir eröffnen einen neune Onlineshop rund um das Thema Gartengeräte, im Sinne von Schläuchen, Schlauchwagen, Gartenbewässerung, Blumenkästen und Co.
Aufgabenstellung
Wir benötigen für diesen Shop ein komplettes Design ( Header,Footer, Menü, Detailansicht, Buttons) welches wir nachher in unseren Kerbel Shop einbinden.
Das Template wird von uns erstellt.
Die farbliche Gestaltung sollte zum Thema passen, hier dürfen also gerne Blau und Grüntöne verwendet werden.
Es soll kein klassisches 3 Spaltenlayout sein, gerne würden wir mit einem 2 Spaltenlayout arbeiten, links mit der Kategoriespalte und dann eine große Produkt und Inhaltsspalte
Der Shop wird den Namen minaru tragen.

```html
<!DOCTYPE html>
<html lang="de">
<head>
<meta charset="utf-8">
<title>minaru – Pflanzenkästen</title>
<link href="https://fonts.googleapis.com/css2?family=Open+Sans:wght@400;600;700;800&display=swap" rel="stylesheet">
<style>
  :root {
    --green: #3cc75a;
    --text: #555555;
    --muted: #8a8a8a;
    --tile: #e8e8e8;
    --sale: #e53935;
    --footer-bg: #222222;
    --footer-text: #ffffff;
    --footer-muted: #9a9a9a;
    --wood: #e39a52;
    --wicker-dark: #3a3c40;
    --leaf: #5f8f3e;
    --pot-light: #eadcd8;
    --metal-red: #b9443f;
    --rack-brown: #5b4a40;
    --wicker-light: #c9a36a;
    --bloom: #b4359a;
  }
  * { margin: 0; padding: 0; box-sizing: border-box; }
  html, body { width: 983px; height: 1200px; overflow: hidden; }
  body { font-family: "Open Sans", sans-serif; color: var(--text); background: #fff; position: relative; }
  a { color: inherit; text-decoration: none; }
  ul { list-style: none; }

  .topbar { position: absolute; top: 0; left: 0; width: 983px; height: 5px; background: var(--green); }

  .logo { position: absolute; left: 129px; top: 17px; font-size: 40px; font-weight: 800; color: var(--green); letter-spacing: 1px; line-height: 1; }

  .service-nav { position: absolute; right: 131px; top: 25px; display: flex; gap: 14px; font-size: 11px; color: var(--muted); }
  .service-nav .cart { color: var(--muted); display: flex; align-items: center; gap: 5px; }

  .main-nav { position: absolute; left: 130px; top: 68px; display: flex; gap: 21px; font-size: 14px; color: var(--muted); letter-spacing: .2px; }
  .main-nav li::after { content: ""; display: inline-block; margin-left: 5px; border-left: 4px solid transparent; border-right: 4px solid transparent; border-top: 6px solid var(--muted); vertical-align: 2px; }

  .search { position: absolute; left: 672px; top: 61px; width: 180px; height: 21px; display: flex; }
  .search-field { flex: 1; background: #d8d8d8; }
  .search-button { width: 31px; background: var(--green); display: flex; align-items: center; justify-content: center; }

  .page-title { position: absolute; left: 0; width: 983px; top: 128px; text-align: center; font-size: 25px; font-weight: 700; color: #444; letter-spacing: .5px; }

  .sort { position: absolute; left: 711px; top: 132px; width: 141px; height: 22px; border: 1px solid #aaa; font-size: 11px; color: #555; padding: 3px 6px; }
  .sort::after { content: ""; position: absolute; right: 6px; top: 8px; border-left: 4px solid transparent; border-right: 4px solid transparent; border-top: 6px solid #999; }

  .product-grid { position: absolute; left: 130px; top: 192px; display: grid; grid-template-columns: repeat(4, 169px); column-gap: 15px; grid-auto-rows: 260px; }
  .product { text-align: center; }
  .product-image { position: relative; width: 169px; height: 169px; background: var(--tile); overflow: hidden; }
  .product-image.trellis { background: radial-gradient(ellipse 30% 45% at 50% 50%, var(--wood) 0%, #e9bd8e 55%, var(--tile) 100%); }
  .product-image.wicker-round { background: radial-gradient(ellipse 38% 40% at 50% 52%, var(--wicker-dark) 0%, #5a5c61 55%, var(--tile) 100%); }
  .product-image.planter-pair { background: radial-gradient(ellipse 45% 30% at 50% 35%, var(--leaf) 0%, #9cb88a 50%, transparent 100%), radial-gradient(ellipse 45% 25% at 50% 75%, var(--pot-light) 0%, var(--tile) 100%); }
  .product-image.metal-bucket { background: radial-gradient(ellipse 30% 40% at 50% 50%, var(--metal-red) 0%, #cf8581 55%, var(--tile) 100%); }
  .product-image.plant-rack { background: radial-gradient(ellipse 45% 20% at 50% 28%, var(--leaf) 0%, #9cb88a 50%, transparent 100%), radial-gradient(ellipse 45% 35% at 50% 60%, var(--rack-brown) 0%, #a69990 50%, var(--tile) 100%); }
  .product-image.plant-tower { background: radial-gradient(ellipse 20% 45% at 50% 50%, var(--leaf) 0%, #a6bb98 55%, var(--tile) 100%); }
  .product-image.wicker-square { background: radial-gradient(ellipse 28% 45% at 50% 50%, var(--wicker-light) 0%, #d9c3a1 55%, var(--tile) 100%); }
  .product-image.flower-box { background: radial-gradient(ellipse 48% 18% at 50% 45%, var(--bloom) 0%, #cf88c0 50%, transparent 100%), radial-gradient(ellipse 48% 12% at 50% 62%, #2e3032 0%, #7d7f81 55%, var(--tile) 100%); }
  .sale-badge { position: absolute; right: 0; top: 0; }
  .product-name { margin-top: 11px; font-size: 12.3px; line-height: 15px; color: #555; }
  .product-price { margin-top: 5px; font-size: 12.3px; color: var(--muted); }
  .product-old-price { font-size: 8px; color: var(--muted); text-decoration: line-through; line-height: 10px; }

  .footer { position: absolute; left: 0; top: 1006px; width: 983px; height: 194px; background: var(--footer-bg); color: var(--footer-text); }
  .footer-col { position: absolute; top: 33px; }
  .footer-col h3 { font-size: 14px; font-weight: 600; letter-spacing: .3px; margin-bottom: 13px; }
  .footer-col li { font-size: 10.8px; line-height: 14px; }
  .newsletter-field { width: 137px; height: 22px; border: 1px solid #fff; font-size: 11px; padding: 3px 6px; position: relative; }
  .newsletter-field::after { content: ""; position: absolute; right: 7px; top: 6px; border-top: 4px solid transparent; border-bottom: 4px solid transparent; border-left: 6px solid #fff; }
  .copyright { position: absolute; left: 0; width: 983px; top: 157px; text-align: center; font-size: 11px; }
  .copyright a { color: var(--footer-muted); }
</style>
</head>
<body>
  <div class="topbar"></div>

  <header>
    <div class="logo">MINARU</div>
    <ul class="service-nav">
      <li><a href="#">HILFE</a></li>
      <li><a href="#">KONTAKT</a></li>
      <li><a href="#">MEIN KONTO</a></li>
      <li><a class="cart" href="#"><svg width="9" height="11" viewBox="0 0 9 11"><path d="M2 5V3.5a2.5 2.5 0 0 1 5 0V5" fill="none" stroke="#3cc75a" stroke-width="1.3"/><rect x="0" y="5" width="9" height="6" fill="#3cc75a"/></svg>WARENKORB (0)</a></li>
    </ul>
    <ul class="main-nav">
      <li>BEWÄSSERUNG</li>
      <li>GARTENGERÄTE</li>
      <li>PFLANZEN</li>
      <li>DEKORATION</li>
    </ul>
    <div class="search">
      <div class="search-field"></div>
      <div class="search-button"><svg width="13" height="13" viewBox="0 0 13 13"><circle cx="5.2" cy="5.2" r="4" fill="none" stroke="#fff" stroke-width="2"/><line x1="8" y1="8" x2="12" y2="12" stroke="#fff" stroke-width="2.2" stroke-linecap="round"/></svg></div>
    </div>
  </header>

  <main>
    <h1 class="page-title">PFLANZENKÄSTEN</h1>
    <div class="sort">Beliebtheit</div>

    <div class="product-grid">
      <div class="product"><div class="product-image trellis" role="img" aria-label="Holzspalier mit Pflanzkasten"></div><p class="product-name">Spalier mit Pflanzkasten</p><p class="product-price">199,95 €</p></div>
      <div class="product"><div class="product-image wicker-round" role="img" aria-label="Rundes dunkles Flecht-Pflanzgefäß"></div><p class="product-name">Pflanzgefäß mit Lenvia,<br>rund</p><p class="product-price">64,95 €</p></div>
      <div class="product"><div class="product-image planter-pair" role="img" aria-label="Zwei Übertöpfe mit grünen Pflanzen"></div><p class="product-name">Pflanzen-Übertopf</p><p class="product-price">59,95 €</p></div>
      <div class="product"><div class="product-image metal-bucket" role="img" aria-label="Roter Metall-Pflanzbehälter mit Haken">
        <svg class="sale-badge" width="45" height="45" viewBox="0 0 45 45"><polygon points="0,0 24,0 45,21 45,45" fill="#e53935"/><text x="28.5" y="16.5" transform="rotate(45 28.5 16.5)" text-anchor="middle" dominant-baseline="central" font-family="Open Sans, sans-serif" font-size="10" font-weight="600" fill="#fff">SALE</text></svg>
      </div><p class="product-name">Metall-Pflanzbehälter</p><p class="product-price">5,95 €</p><p class="product-old-price">14,95 €</p></div>

      <div class="product"><div class="product-image plant-rack" role="img" aria-label="Metallgestell mit drei bepflanzten Töpfen"></div><p class="product-name">Pflanzgefäß „Nature“ (4-tlg.)</p><p class="product-price">39,95 €</p></div>
      <div class="product"><div class="product-image plant-tower" role="img" aria-label="Hohes Metallgestell mit zwei Töpfen"></div><p class="product-name">Pflanzgefäß „Noire“ (2 Stk.)</p><p class="product-price">24,95 €</p></div>
      <div class="product"><div class="product-image wicker-square" role="img" aria-label="Eckiges Pflanzgefäß aus Naturgeflecht"></div><p class="product-name">Pflanzgefäß mit Lenvia,<br>quadratisch</p><p class="product-price">ab 64,95 €</p></div>
      <div class="product"><div class="product-image flower-box" role="img" aria-label="Dunkler Blumenkasten mit pinken Blüten"></div><p class="product-name">Blumenkasten „Landhaus“</p><p class="product-price">19,95 €</p></div>

      <div class="product"><div class="product-image trellis" role="img" aria-label="Holzspalier mit Pflanzkasten"></div><p class="product-name">Spalier mit Pflanzkasten</p><p class="product-price">199,95 €</p></div>
      <div class="product"><div class="product-image wicker-round" role="img" aria-label="Rundes dunkles Flecht-Pflanzgefäß"></div><p class="product-name">Pflanzgefäß mit Lenvia,<br>rund</p><p class="product-price">64,95 €</p></div>
      <div class="product"><div class="product-image planter-pair" role="img" aria-label="Zwei Übertöpfe mit grünen Pflanzen"></div><p class="product-name">Pflanzen-Übertopf</p><p class="product-price">59,95 €</p></div>
      <div class="product"><div class="product-image metal-bucket" role="img" aria-label="Roter Metall-Pflanzbehälter mit Haken">
        <svg class="sale-badge" width="45" height="45" viewBox="0 0 45 45"><polygon points="0,0 24,0 45,21 45,45" fill="#e53935"/><text x="28.5" y="16.5" transform="rotate(45 28.5 16.5)" text-anchor="middle" dominant-baseline="central" font-family="Open Sans, sans-serif" font-size="10" font-weight="600" fill="#fff">SALE</text></svg>
      </div><p class="product-name">Metall-Pflanzbehälter</p><p class="product-price">5,95 €</p><p class="product-old-price">14,95 €</p></div>
    </div>
  </main>

  <footer class="footer">
    <div class="footer-col" style="left:130px"><h3>KATEGORIEN</h3><ul><li>BEWÄSSERUNG</li><li>GARTENGERÄTE</li><li>PFLANZEN</li><li>DEKORATION</li></ul></div>
    <div class="footer-col" style="left:275px"><h3>BESTELLUNG</h3><ul><li>VERSAND &amp; LIEFERUNG</li><li>BEZAHLUNG</li><li>WIDERRUFSRECHT</li><li>AGB</li><li>DATENSCHUTZ</li></ul></div>
    <div class="footer-col" style="left:419px"><h3>ÜBER UNS</h3><ul><li>FILIALE</li><li>JOBS</li><li>HINSTORIE</li><li>IMPRESSUM</li></ul></div>
    <div class="footer-col" style="left:564px"><h3>SUPPORT</h3><ul><li>FAQ</li><li>KONTAKT</li></ul></div>
    <div class="footer-col" style="left:707px"><h3>NEWSLETTER</h3><div class="newsletter-field">deine email</div></div>
    <p class="copyright">© 2013 MINARU INC. <a href="#">TERMS OF USE</a> | <a href="#">PRIVACY POLICY</a></p>
  </footer>
</body>
</html>
```